Velmor Partners - website for real estate investment company

Create a bold, modern website that reflects Velmor’s success, professionalism, and credibility.
The design must stand out while maintaining a polished, corporate tone. (bold, but understated)
The client just created a new logo, and the website design must be in sync with the logo design. Information about the logo colors, fonts, and message are in the attached design brief.

Target Market(s)

b2b: banks, brokers, institutional partners, vendors, and property sellers.

Industry/Entity Type

real estate investment company

Number of Pages Required

1 page

Font styles to use
Sans Serif

Colors

Designer to choose colors to be used in the design.

Requirements
Must have
• 1. homepage design (psd) 2. a top banner image (psd) for a default inner page
Nice to have
• please see attached design brief
Should not have

```html
<!DOCTYPE html>
<html lang="en">
<head>
<meta charset="utf-8">
<title>Velmor Partners — Real Estate Investment Excellence</title>
<link rel="stylesheet" href="https://fonts.googleapis.com/css2?family=Barlow:wght@400;500;600;700;800&family=Mrs+Saint+Delafield&display=swap">
<style>
:root{
  --red:#e01e26;
  --red-dark:#c4161d;
  --ink:#3a3a3c;
  --text:#333336;
  --muted:#666;
  --light:#f1f1f1;
  --line:#dcdcdc;
  --footer:#3b3b3d;
  --white:#fff;
}
*{box-sizing:border-box;margin:0;padding:0}
html,body{width:1200px;height:3989px;overflow:hidden}
body{position:relative;font-family:"Barlow",Arial,sans-serif;color:var(--text);background:var(--white)}
.abs{position:absolute}
.btn{position:absolute;display:flex;align-items:center;justify-content:center;font-weight:600;font-size:13px;letter-spacing:.3px;text-transform:uppercase;color:var(--white);background:var(--red);text-decoration:none}
.btn-outline{background:transparent;border:1px solid rgba(255,255,255,.8)}
.script{position:absolute;font-family:"Mrs Saint Delafield",cursive;color:var(--red);font-size:58px;line-height:1}
.section-title{position:absolute;font-weight:700;font-size:36px;color:var(--ink);letter-spacing:.5px;text-transform:uppercase}
.center{left:0;width:1200px;text-align:center}

/* hero */
.hero{position:absolute;left:0;top:0;width:1200px;height:720px;background:linear-gradient(180deg,#5f8fc4 0%,#9cbad7 22%,#7c8f93 40%,#5c6a5c 62%,#3b4238 100%)}
.hero-shade{position:absolute;inset:0;background:linear-gradient(180deg,rgba(0,0,0,.15) 0%,rgba(0,0,0,.05) 30%,rgba(0,0,0,.35) 70%,rgba(0,0,0,.55) 100%)}
.topline{position:absolute;left:0;top:0;width:1200px;height:4px;background:var(--red)}
.logo{position:absolute;font-weight:800;font-size:48px;letter-spacing:1px;color:var(--white);line-height:1}
.nav{position:absolute;left:402px;top:34px;display:flex;gap:20px}
.nav a{color:var(--white);font-weight:600;font-size:12.5px;letter-spacing:.6px;text-decoration:none;text-transform:uppercase}
.hero-script{position:absolute;top:312px;font-family:"Mrs Saint Delafield",cursive;color:var(--white);font-size:52px}
.hero-title{position:absolute;top:375px;font-weight:700;font-size:44px;color:var(--white);letter-spacing:.5px}
.hero-text{position:absolute;left:220px;top:428px;width:760px;text-align:center;color:var(--white);font-size:14px;line-height:22px}

/* stats */
.stat{position:absolute;top:724px;width:283px;height:223px;background:var(--white);box-shadow:0 4px 18px rgba(0,0,0,.12);border-bottom:3px solid var(--red);text-align:center}
.stat svg{margin-top:22px}
.stat-num{font-weight:700;font-size:44px;color:var(--red);line-height:1;margin-top:10px}
.stat-label{font-size:12.5px;font-weight:500;color:var(--ink);margin-top:8px;text-transform:uppercase}
.stat-sub{font-size:12.5px;color:var(--ink);margin-top:3px}

/* about */
.photo{position:absolute}
.about-text{position:absolute;left:541px;top:1122px;width:520px;font-size:12.5px;line-height:24.5px;color:var(--text)}
.badge{position:absolute;left:990px;top:1243px;width:106px;height:106px;border-radius:50%;background:var(--red)}

/* portfolio */
.portfolio{position:absolute;left:0;top:1710px;width:1200px;height:1172px;background:var(--light)}
.tile{position:absolute;overflow:hidden}
.tile-overlay{position:absolute;inset:0;background:rgba(0,0,0,.35);color:var(--white);text-align:center}

/* contact */
.field{position:absolute;height:54px;border:1px solid var(--line);background:var(--white);display:flex;align-items:center;padding-left:16px;font-size:11.5px;color:#888}
.field .sep{width:1px;height:20px;background:var(--line);margin:0 12px}

/* footer */
.footer-h{position:absolute;font-weight:700;font-size:14px;color:var(--white);letter-spacing:.4px;text-transform:uppercase}
.footer-t{position:absolute;font-size:12.5px;color:#e4e4e4;line-height:20px}
.qlinks{position:absolute;left:488px;top:3675px;list-style:none}
.qlinks li{font-size:13px;color:#e4e4e4;height:28px}
.social{position:absolute;left:954px;display:flex;align-items:center;gap:10px;font-size:13px;color:#e4e4e4}
.social span.dot{width:30px;height:30px;border:1.5px solid #e4e4e4;border-radius:50%}
</style>
</head>
<body>

<!-- HERO -->
<section class="hero" role="img" aria-label="Aerial view of a city skyline with a domed capitol building and green trees">
  <div class="hero-shade"></div>
</section>
<div class="topline"></div>
<div class="logo" style="left:140px;top:22px">VELMOR</div>
<nav class="nav">
  <a href="#">Home</a><a href="#">Our Story</a><a href="#">Investment Strategy</a><a href="#">What Sets Us Apart</a><a href="#">Portfolio</a>
</nav>
<a class="btn" href="#" style="left:949px;top:21px;width:107px;height:42px;font-size:12.5px">Contact Us</a>

<div class="hero-script center">Experience – Strategy – Vision</div>
<h1 class="hero-title center">REAL ESTATE INVESTMENT EXCELLENCE</h1>
<p class="hero-text">Velmor Partners Is A Vertically Integrated Real Estate Investment Firm With A Proven Four-Decade Track Record. We Acquire, Reposition, And Operate High-Performing Assets Across Multiple Sectors — Always With A Focus On Exceptional, Risk-Adjusted Returns.</p>
<a class="btn" href="#" style="left:401px;top:510px;width:187px;height:50px">Explore Our Portfolio</a>
<a class="btn btn-outline" href="#" style="left:602px;top:510px;width:145px;height:50px">Partner With Us</a>

<svg class="abs" style="left:0;top:575px" width="1200" height="150" viewBox="0 0 1200 150">
  <polygon points="0,145 0,150 1200,150 1200,90 0,90" fill="#fff"/>
  <polygon points="0,75 0,145 200,75" fill="#d9d9d9"/>
  <polygon points="0,75 0,150 1200,150 1200,65 1000,40 300,75" fill="#fff"/>
  <polygon points="890,25 1200,0 1200,130" fill="var(--red)"/>
  <polygon points="0,65 0,145 200,75" fill="#d8d8d8"/>
</svg>

<!-- STATS -->
<div class="stat" style="left:141px">
  <svg width="64" height="64" viewBox="0 0 64 64" fill="none" stroke="#444" stroke-width="2"><rect x="14" y="10" width="36" height="50"/><rect x="24" y="4" width="16" height="6"/><path d="M20 18h6M30 18h4M38 18h6M20 26h6M38 26h6M20 34h6M38 34h6M20 42h6M38 42h6"/><circle cx="32" cy="34" r="5"/><rect x="27" y="46" width="10" height="14"/><path d="M8 60h48"/></svg>
  <div class="stat-num">1989</div>
  <div class="stat-label">Founded</div>
  <div class="stat-sub">Over 4 Decades Of Expertise</div>
</div>
<div class="stat" style="left:458px">
  <svg width="76" height="64" viewBox="0 0 76 64" fill="none" stroke="#444" stroke-width="2"><circle cx="32" cy="28" r="18"/><path d="M32 4v6M32 46v6M8 28h6M50 28h6M15 11l4 4M45 41l4 4M49 11l-4 4"/><path d="M28 40l20-16 20 16M32 37v23h32V37"/><rect x="44" y="46" width="8" height="14"/></svg>
  <div class="stat-num">23,000+</div>
  <div class="stat-label">Units Managed</div>
  <div class="stat-sub">Multifamily &amp; Healthcare Properties</div>
</div>
<div class="stat" style="left:776px">
  <svg width="70" height="64" viewBox="0 0 70 64" fill="none" stroke="#444" stroke-width="2"><circle cx="24" cy="20" r="9"/><path d="M8 60V46c0-8 7-13 16-13s16 5 16 13v14"/><path d="M20 34l4 10 4-10"/><circle cx="48" cy="14" r="10"/><path d="M51 10h-5a2 2 0 0 0 0 4h4a2 2 0 0 1 0 4h-5M48 8v12"/><rect x="42" y="40" width="18" height="4"/><rect x="44" y="46" width="18" height="4"/><rect x="42" y="52" width="18" height="4"/></svg>
  <div class="stat-num">$300M+</div>
  <div class="stat-label">Invested In Renovations</div>
  <div class="stat-sub">Continuous Property Improvement</div>
</div>

<!-- ABOUT -->
<div class="photo" role="img" aria-label="Three business professionals reviewing a document in a bright office" style="left:141px;top:1036px;width:326px;height:384px;background:linear-gradient(160deg,#8a7a68,#cfc6b8 45%,#6e6456)"></div>
<div class="photo" role="img" aria-label="Light pencil sketch of a two-storey house" style="left:10px;top:1450px;width:470px;height:220px;background:linear-gradient(180deg,#fafafa,#f0f0f0)"></div>
<div class="script" style="left:538px;top:1030px">About</div>
<h2 class="section-title" style="left:538px;top:1074px">Velmor Partners</h2>
<p class="about-text">Velmor Partners Is A Real Estate Investment Company That Has Been Successfully Buying, Improving, And Managing Properties For Over 40 Years. We Focus On Making Smart Investments In Different Types Of Real Estate To Deliver Strong, Reliable Returns While Carefully Managing Risk.</p>
<a class="btn" href="#" style="left:541px;top:1231px;width:104px;height:41px">Read More</a>
<div class="photo" role="img" aria-label="Hands of a businessman over contract papers beside a small model house" style="left:541px;top:1308px;width:518px;height:267px;background:linear-gradient(120deg,#3a2a22,#8e6a52 45%,#d9cfc6)"></div>
<div class="badge"></div>
<svg class="abs" style="left:990px;top:1243px" width="106" height="106" viewBox="0 0 106 106">
  <circle cx="53" cy="53" r="34" fill="none" stroke="#fff" stroke-width="2"/>
  <circle cx="53" cy="53" r="26" fill="#fff"/>
  <text x="53" y="64" text-anchor="middle" font-family="Barlow, sans-serif" font-weight="700" font-size="30" fill="#e01e26">40</text>
  <defs><path id="ring" d="M53 53 m-42 0 a42 42 0 1 1 84 0 a42 42 0 1 1 -84 0"/></defs>
  <text font-family="Barlow, sans-serif" font-weight="700" font-size="10" letter-spacing="3" fill="#fff"><textPath href="#ring" startOffset="2%">YEAR OF EXPERIENCE</textPath></text>
</svg>

<!-- PORTFOLIO -->
<section class="portfolio"></section>
<div class="script center" style="top:1780px">Photo Gallery</div>
<h2 class="section-title center" style="top:1836px">Our Portfolio</h2>

<div class="tile" role="img" aria-label="Modern living room interior with sofa and open kitchen" style="left:141px;top:1918px;width:291px;height:416px;background:linear-gradient(180deg,#f2eee8,#d8cfc4 55%,#9c8f80)"></div>
<div class="tile" style="left:455px;top:1918px;width:291px;height:416px;background:linear-gradient(180deg,#6e9bd0,#4e6e94 50%,#7b7f78)" role="img" aria-label="Glass-fronted healthcare building against a blue sky">
  <div class="tile-overlay">
    <div style="position:absolute;top:266px;left:0;width:291px;font-weight:600;font-size:22px;line-height:26px">MERIDIAN<br>HEALTHCARE CENTER</div>
    <div style="position:absolute;top:326px;left:0;width:291px;font-size:11px">State-of-the-art medical facility in Austin, TX</div>
    <div style="position:absolute;left:85px;top:356px;width:118px;height:38px;border:1px solid #fff;display:flex;align-items:center;justify-content:center;font-weight:600;font-size:12px">VIEW DETAILS</div>
  </div>
</div>
<div class="tile" role="img" aria-label="Low glass office building on a green lawn" style="left:768px;top:1918px;width:291px;height:224px;background:linear-gradient(180deg,#3d86d6,#9cc6ea 45%,#5f7e4a 75%,#4e8a32)"></div>
<div class="tile" role="img" aria-label="Contemporary house with wood cladding and a wooden deck" style="left:768px;top:2159px;width:291px;height:367px;background:linear-gradient(180deg,#b8d3ec,#c9b59a 50%,#8b6b4c 80%,#6f8a5a)"></div>
<div class="tile" role="img" aria-label="Modern tower with red glass facade at sunset" style="left:141px;top:2352px;width:291px;height:365px;background:linear-gradient(180deg,#8aaecc,#7a5a70 45%,#3c2e34)"></div>
<div class="tile" role="img" aria-label="Dark suburban home with flowering garden and lawn" style="left:455px;top:2352px;width:291px;height:365px;background:linear-gradient(180deg,#a9c7e6,#4d5560 45%,#5d7a3c 80%,#4c8a2c)"></div>
<div class="tile" role="img" aria-label="Modern villa with lit windows at dusk" style="left:768px;top:2542px;width:291px;height:175px;background:linear-gradient(180deg,#b6cbe0,#e8d8b8 45%,#3e4a3a 80%,#4f7a3a)"></div>

<a class="btn" href="#" style="left:520px;top:2754px;width:159px;height:42px;font-size:12.5px">View All Portfolio</a>

<!-- CONTACT -->
<svg class="abs" style="left:0;top:3310px" width="1200" height="280" viewBox="0 0 1200 280" aria-hidden="true">
  <g fill="#ededed">
    <rect x="40" y="110" width="50" height="170"/><rect x="100" y="60" width="36" height="220"/><rect x="180" y="20" width="22" height="260"/><rect x="150" y="90" width="40" height="190"/><rect x="215" y="130" width="60" height="150"/><rect x="0" y="150" width="40" height="130"/>
    <rect x="920" y="120" width="60" height="160"/><rect x="960" y="30" width="40" height="250"/><rect x="1010" y="80" width="50" height="200"/><rect x="1070" y="140" width="60" height="140"/><rect x="1140" y="100" width="60" height="180"/>
  </g>
</svg>
<div class="script center" style="top:2965px">Contact Us</div>
<h2 class="section-title center" style="top:3014px">Get In Touch</h2>
<p class="abs center" style="top:3068px;font-size:12.5px;color:var(--ink)">Reach Out To Discuss Partnership Opportunities Or Learn More About Our Investment Approach.</p>

<div class="field" style="left:292px;top:3106px;width:300px"><svg width="14" height="14" viewBox="0 0 14 14" fill="none" stroke="#999"><circle cx="7" cy="4.5" r="3"/><path d="M1.5 13c0-3 2.5-5 5.5-5s5.5 2 5.5 5"/></svg><span class="sep"></span>First Name</div>
<div class="field" style="left:607px;top:3106px;width:300px"><svg width="14" height="14" viewBox="0 0 14 14" fill="none" stroke="#999"><circle cx="7" cy="4.5" r="3"/><path d="M1.5 13c0-3 2.5-5 5.5-5s5.5 2 5.5 5"/></svg><span class="sep"></span>Last Name</div>
<div class="field" style="left:292px;top:3174px;width:300px"><svg width="14" height="14" viewBox="0 0 14 14" fill="none" stroke="#999"><rect x="1" y="3" width="12" height="9"/><path d="M1 3l6 5 6-5"/></svg><span class="sep"></span>Your Email</div>
<div class="field" style="left:607px;top:3174px;width:300px"><svg width="14" height="14" viewBox="0 0 14 14" fill="none" stroke="#999"><path d="M3 1l2.5 3-1.5 1.5a8 8 0 0 0 4.5 4.5L10 8.5l3 2.5-1.5 2C6 13 1 8 1 2.5z"/></svg><span class="sep"></span>Phone</div>
<div class="field" style="left:292px;top:3242px;width:615px;height:123px;align-items:flex-start;padding-top:18px"><svg width="14" height="14" viewBox="0 0 14 14" fill="none" stroke="#999"><path d="M1 2h12v8H5l-3 3v-3H1z"/></svg><span class="sep" style="height:14px"></span>Your Message</div>
<a class="btn" href="#" style="left:292px;top:3373px;width:615px;height:52px;font-size:13px">Submit Now</a>

<!-- FOOTER -->
<svg class="abs" style="left:0;top:3460px" width="1200" height="529" viewBox="0 0 1200 529">
  <polygon points="0,0 310,125 0,130" fill="var(--red)"/>
  <polygon points="1200,15 1200,60 990,90" fill="#d4d4d4"/>
  <polygon points="0,130 310,125 1200,45 1200,529 0,529" fill="var(--footer)"/>
</svg>

<div class="logo" style="left:140px;top:3650px;font-size:46px">VELMOR</div>
<p class="footer-t" style="left:141px;top:3704px;width:240px;font-size:12px;line-height:19px">Velmor Partners Is A Real Estate Investment Company That Has Been Successfully Buying, Improving, And Managing Properties For Over 40 Years.</p>
<div class="footer-h" style="left:141px;top:3800px">Career Opportunities</div>
<a class="btn" href="#" style="left:141px;top:3828px;width:102px;height:36px;font-size:12px;gap:5px"><svg width="13" height="10" viewBox="0 0 13 10"><rect width="13" height="10" fill="#fff"/><path d="M0 0l6.5 5L13 0" fill="none" stroke="#e01e26" stroke-width="1.3"/></svg>Email Us</a>

<div class="footer-h" style="left:487px;top:3647px">Quick Links</div>
<ul class="qlinks">
  <li>Home</li><li>Our Story</li><li>Investment Strategy</li><li>What Sets Us Apart</li><li>Our Portfolio</li><li>Contact Us</li>
</ul>

<div class="footer-h" style="left:683px;top:3647px">Contact Details</div>
<svg class="abs" style="left:684px;top:3678px" width="12" height="16" viewBox="0 0 12 16"><path d="M6 0a6 6 0 0 0-6 6c0 4.5 6 10 6 10s6-5.5 6-10a6 6 0 0 0-6-6z" fill="#fff"/><circle cx="6" cy="6" r="2.3" fill="var(--footer)"/></svg>
<p class="footer-t" style="left:704px;top:3676px">410 Harbor Crest Ave.<br>Suite 12, Lakemont, NJ</p>
<svg class="abs" style="left:683px;top:3727px" width="13" height="13" viewBox="0 0 14 14"><path d="M3 1l2.5 3-1.5 1.5a8 8 0 0 0 4.5 4.5L10 8.5l3 2.5-1.5 2C6 13 1 8 1 2.5z" fill="#fff"/></svg>
<p class="footer-t" style="left:704px;top:3724px"><b style="color:#fff">Phone</b><br>+1 555 014 2290</p>
<svg class="abs" style="left:683px;top:3780px" width="13" height="10" viewBox="0 0 13 10"><rect width="13" height="10" fill="#fff"/><path d="M0 0l6.5 5L13 0" fill="none" stroke="var(--footer)" stroke-width="1.3"/></svg>
<p class="footer-t" style="left:704px;top:3776px"><b style="color:#fff">General Inquiries</b><br>info@velmorpartners.example</p>

<div class="footer-h" style="left:955px;top:3647px">Social Media</div>
<div class="social" style="top:3674px"><span class="dot"></span>Connectly</div>
<div class="social" style="top:3715px"><span class="dot"></span>Vidora</div>
<div class="social" style="top:3756px"><span class="dot"></span>Proflink</div>
<div class="social" style="top:3797px"><span class="dot"></span>Snapwall</div>

<div class="abs" style="left:141px;top:3930px;width:918px;height:1px;background:#5a5a5c"></div>
<p class="abs center" style="top:3953px;font-size:12.5px;color:#e4e4e4">© 2025 Velmor Partners. All Rights Reserved.</p>

</body>
</html>
```